Revamping and duplicating of existing business card

We are a painting and decorating business based in London and need a couple of business cards made up for the following people.

1. Marla Penhallow
2. Toby Renwick

Measurements - 85 X 55 mm
Font: Blue highway
Colour: No idea! Would be great to have a pantone for the pink if possible?

I’ve attached all the logos and old artwork etc.
Here are the amendments I would definitely like...

1. Marla

format mobile number correctly: 07451 386 902

Add title: Decorator
Use: Penhallow Decorating Logo
Add twitter logo & @penhallowdecor
Add tradeverify logo
Add HFG Logo
Make it all look beautiful/revamp/tweak - whatever you think…

2. Toby

Decorator

07623 519 840
toby@penhallowdecorating.co.uk
Updates

Hello! Thanks so much for all your designs. This is such a great way to get these things done... Just to clarify, Please do not alter our logo at all. The 'splat' appears on our van, tshirts, quotes etc and is very much part of our branding. Colour scheme: Pink, black and white. Thanks Marla

Reason: Not 100% sold on any of the designs so far but very grateful for all the submissions. Keep it simple and quirky please. Thanks Marla

Industry/Entity Type

Painting

Requirements
Must have
• Pink & Black Colour scheme
Penhallow Decorating Logo
Blue Highway font

```html
<!DOCTYPE html>
<html lang="en">
<head>
<meta charset="utf-8">
<title>Penhallow Decorating – Business Cards</title>
<link href="https://fonts.googleapis.com/css2?family=Oswald:wght@400;500;600&display=swap" rel="stylesheet">
<style>
  :root {
    --pink: #b0245a;
    --paper: #e1e0e1;
    --navy: #2a2f6e;
    --blue: #2b6cb0;
    --red: #d4312f;
    --white: #ffffff;
    --page: #ffffff;
    --edge: #9a9aa8;
  }
  * { box-sizing: border-box; margin: 0; padding: 0; }
  html, body { width: 1200px; height: 761px; overflow: hidden; background: var(--page); }
  body { position: relative; font-family: "Oswald", sans-serif; }

  .card {
    position: absolute; width: 454px; height: 304px;
    background: var(--paper); border: 1px solid var(--edge); overflow: hidden;
  }
  .card--front-a { left: 42px; top: 36px; }
  .card--front-b { left: 692px; top: 36px; }
  .card--back-a  { left: 40px; top: 411px; }
  .card--back-b  { left: 689px; top: 409px; }

  /* front */
  .front__field { position: absolute; inset: 0 0 88px 0; background: var(--pink); }
  .front__disc {
    position: absolute; left: 118px; top: 22px; width: 190px; height: 190px;
    border-radius: 50%; background: var(--paper);
  }
  .wordmark {
    position: absolute; left: 0; right: 0; top: 88px; text-align: center;
    color: var(--navy); font-weight: 600; line-height: 1; letter-spacing: 0.5px;
  }
  .wordmark__top { display: block; font-size: 34px; }
  .wordmark__bottom { display: block; font-size: 23px; margin-top: 2px; }
  .front__strip {
    position: absolute; left: 0; right: 0; bottom: 0; height: 88px;
    background: var(--paper); border-radius: 8px 8px 0 0;
  }
  .member-badge {
    position: absolute; left: 26px; top: 10px; width: 68px; height: 70px;
    border-radius: 40% 40% 48% 48%; background: var(--white); border: 5px solid var(--navy);
  }
  .membership { position: absolute; right: 20px; top: 20px; text-align: right; line-height: 1; }
  .membership__label { display: block; font-size: 9px; color: #222; margin-bottom: 6px; padding-right: 60px; }
  .membership__name { font-size: 21px; font-weight: 500; color: var(--red); }

  /* back */
  .ornament {
    position: absolute; left: 135px; top: 56px; width: 195px; height: 80px;
    background: var(--pink); border-radius: 90px 90px 20px 20px;
  }
  .card--back-b .ornament { left: 134px; top: 60px; }
  .person { position: absolute; left: 0; right: 0; top: 134px; text-align: center; line-height: 1; }
  .card--back-b .person { top: 136px; }
  .person__name {
    display: block; font-size: 31px; font-weight: 600; color: var(--navy);
    text-shadow: 1px 2px 2px rgba(0,0,0,0.35);
  }
  .person__role { display: block; font-size: 13px; font-weight: 600; color: var(--blue); margin-top: 4px; letter-spacing: 0.5px; }
  .contact {
    position: absolute; left: 0; right: 0; bottom: 0; height: 84px;
    background: var(--pink); border-radius: 4px 4px 0 0; padding: 8px 0 0 10px;
    list-style: none;
  }
  .card--back-b .contact { height: 86px; padding-top: 20px; }
  .contact__line {
    display: flex; align-items: center; gap: 12px; height: 24.5px;
    color: var(--white); font-size: 16px; font-weight: 400; letter-spacing: 0.4px;
  }
  .contact__icon { width: 22px; height: 20px; flex: none; }
</style>
</head>
<body>

<section class="card card--front-a" aria-label="Front of card">
  <div class="front__field"></div>
  <div class="front__disc"></div>
  <h1 class="wordmark"><span class="wordmark__top">PENHALLOW</span><span class="wordmark__bottom">DECORATING</span></h1>
  <div class="front__strip">
    <div class="member-badge" role="img" aria-label="HFG membership badge"></div>
    <p class="membership"><span class="membership__label">Proud members of</span><span class="membership__name">tradeverify</span></p>
  </div>
</section>

<section class="card card--front-b" aria-label="Front of card">
  <div class="front__field"></div>
  <div class="front__disc"></div>
  <h1 class="wordmark"><span class="wordmark__top">PENHALLOW</span><span class="wordmark__bottom">DECORATING</span></h1>
  <div class="front__strip">
    <div class="member-badge" role="img" aria-label="HFG membership badge"></div>
    <p class="membership"><span class="membership__label">Proud members of</span><span class="membership__name">tradeverify</span></p>
  </div>
</section>

<section class="card card--back-a" aria-label="Back of card, Marla Penhallow">
  <div class="ornament" role="img" aria-label="Pink baroque scroll ornament"></div>
  <h2 class="person"><span class="person__name">MARLA PENHALLOW</span><span class="person__role">DECORATOR</span></h2>
  <ul class="contact">
    <li class="contact__line">
      <svg class="contact__icon" viewBox="0 0 22 20" aria-hidden="true"><circle cx="11" cy="10" r="9" fill="none" stroke="#fff" stroke-width="1.6"/><path d="M8 5.5c-1.5 1-1.5 3 0 5.5s3.5 4 5.5 3.5l.8-1.5-2-1.2-1 .8c-1-.6-2-1.8-2.4-3l1-.7-.7-2.2z" fill="#fff"/></svg>
      07451 386 902
    </li>
    <li class="contact__line">
      <svg class="contact__icon" viewBox="0 0 22 20" aria-hidden="true"><circle cx="11" cy="10" r="7" fill="#fff"/></svg>
      @PENHALLOWDECOR
    </li>
    <li class="contact__line">
      <svg class="contact__icon" viewBox="0 0 22 20" aria-hidden="true"><rect x="1" y="3" width="20" height="14" rx="1" fill="#fff"/><path d="M1.5 4l9.5 7 9.5-7" fill="none" stroke="#b0245a" stroke-width="1.4"/></svg>
      MARLA@PENHALLOWDECORATING.CO.UK
    </li>
  </ul>
</section>

<section class="card card--back-b" aria-label="Back of card, Toby Renwick">
  <div class="ornament" role="img" aria-label="Pink baroque scroll ornament"></div>
  <h2 class="person"><span class="person__name">TOBY RENWICK</span><span class="person__role">DECORATOR</span></h2>
  <ul class="contact">
    <li class="contact__line">
      <svg class="contact__icon" viewBox="0 0 22 20" aria-hidden="true"><circle cx="11" cy="10" r="9" fill="none" stroke="#fff" stroke-width="1.6"/><path d="M8 5.5c-1.5 1-1.5 3 0 5.5s3.5 4 5.5 3.5l.8-1.5-2-1.2-1 .8c-1-.6-2-1.8-2.4-3l1-.7-.7-2.2z" fill="#fff"/></svg>
      07623 519 840
    </li>
    <li class="contact__line">
      <svg class="contact__icon" viewBox="0 0 22 20" aria-hidden="true"><rect x="1" y="3" width="20" height="14" rx="1" fill="#fff"/><path d="M1.5 4l9.5 7 9.5-7" fill="none" stroke="#b0245a" stroke-width="1.4"/></svg>
      TOBY@PENHALLOWDECORATING.CO.UK
    </li>
  </ul>
</section>

</body>
</html>
```